Website Design for Employee Moral and Happiness Company

Looking for a clean website design that explains our features in a step by step manner so our visitors know exactly what our site does before logging in.

The site is called "Velasto". See logo design and video for a sample of style and an overview of what we do.

Target Market(s)

Business owners that are looking to retain employees.

Number of Pages Required

1 page

```html
<!DOCTYPE html>
<html lang="en">
<head>
<meta charset="utf-8">
<title>Velasto — Increase Employee Retention</title>
<link href="https://fonts.googleapis.com/css2?family=Arvo:wght@400;700&family=Open+Sans:ital,wght@0,400;0,600;0,700;1,400&display=swap" rel="stylesheet">
<style>
:root{
  --orange:#ff6a0d;
  --orange-deep:#f25c00;
  --navy:#1c2f52;
  --navy-dark:#15233f;
  --ink:#1f1f1f;
  --charcoal:#2b2b2b;
  --text:#555;
  --white:#fff;
  --cream:#fdf1e8;
  --footer:#171717;
}
*{box-sizing:border-box;margin:0;padding:0}
html,body{width:1200px;height:4736px;overflow:hidden}
body{font-family:"Open Sans",sans-serif;color:var(--ink);background:var(--white);position:relative}
.abs{position:absolute}
.heading{font-family:"Arvo",serif;font-weight:700}
.btn{position:absolute;background:var(--orange);color:var(--white);font-weight:700;font-size:15px;border-radius:24px;display:flex;align-items:center;justify-content:center}
.para{font-size:14px;line-height:24px;color:var(--text)}

.topbar{top:0;left:0;width:1200px;height:48px;background:var(--navy-dark)}
.topbar-accent{top:0;left:0}
.topbar .contact{position:absolute;color:var(--white);font-size:13px;line-height:16px}
.round-ico{position:absolute;width:26px;height:26px;border-radius:50%;background:var(--orange);display:flex;align-items:center;justify-content:center}
.question-pill{position:absolute;left:812px;top:4px;width:230px;height:38px;border-radius:20px;background:#111}

.nav{top:48px;left:0;width:1200px;height:70px;background:var(--white);border-bottom:1px solid #ddd}
.logo{position:absolute;font-family:"Arvo",serif;font-weight:700;letter-spacing:1px}
.nav-links{position:absolute;right:158px;top:24px;display:flex;gap:44px;font-size:14px;font-weight:600;color:var(--ink)}
.nav-links .active{color:var(--orange)}

.hero{top:118px;left:0;width:1200px;height:544px;background:linear-gradient(120deg,#3b3531,#5c4f45 45%,#3a3b40);overflow:hidden}
.hero-title{position:absolute;top:95px;width:1200px;text-align:center;color:var(--white);font-size:50px;line-height:58px;letter-spacing:1px}
.hero-sub{position:absolute;top:222px;width:1200px;text-align:center;color:var(--white);font-size:22px;line-height:32px;font-weight:600}
.arrow-btn{position:absolute;width:32px;height:32px;border-radius:50%;background:var(--white);display:flex;align-items:center;justify-content:center}

.section-title{font-family:"Arvo",serif;font-weight:700;font-size:40px;color:var(--ink)}
.dots{position:absolute;background-image:radial-gradient(#222 1.6px,transparent 2px);background-size:14px 14px}

.schedule{top:1150px;left:0;width:1200px;height:490px;background:var(--navy)}
.calendar{position:absolute;left:588px;top:1261px;width:436px;height:316px;background:var(--white);padding:12px 6px 10px}
.calendar table{width:100%;border-collapse:collapse;font-family:Arial,sans-serif}
.calendar caption{font-size:40px;line-height:40px;border:2px solid #000;border-bottom:none}
.calendar th{font-size:11px;font-weight:400;border:2px solid #000;height:16px}
.calendar td{font-size:10px;border:2px solid #000;height:46px;vertical-align:top;text-align:right;padding:2px 3px;width:14.28%}
.calendar td.mute{color:#aaa}

.why{top:1640px;left:0;width:1200px;height:560px;background:var(--white);overflow:hidden}
.feature{position:absolute;width:285px;height:118px}
.feature .pill{position:absolute;top:8px;width:285px;height:110px;background:var(--charcoal);border-radius:55px}
.feature .frame{position:absolute;top:0;width:255px;height:118px;border:3px solid var(--orange)}
.feature .txt{position:absolute;top:28px;width:150px;text-align:right;color:var(--white)}
.feature .txt b{display:block;font-family:"Arvo",serif;font-size:17px;letter-spacing:.5px}
.feature .txt span{font-size:14px;line-height:19px}
.feature .ico{position:absolute;top:20px;width:86px;height:86px;border-radius:50%;background:var(--white);display:flex;align-items:center;justify-content:center}

.how{top:2200px;left:0;width:1200px;height:432px;background:linear-gradient(110deg,#2d2d2d,#3a3a3a 50%,#262626)}

.event-date{position:absolute;font-size:14px;font-weight:700;display:flex;align-items:center;gap:6px}
.event-title{position:absolute;font-family:"Arvo",serif;font-weight:700;font-size:19px;line-height:28px}
.photo{position:absolute;border:3px solid #e9e9e9;box-shadow:0 2px 6px rgba(0,0,0,.25)}

.contact-sec{top:3290px;left:0;width:1200px;height:500px;background:linear-gradient(120deg,#f26710,#e8600f 50%,#f27216);overflow:hidden}
.field{position:absolute;background:var(--white);border-radius:6px;font-size:12px;color:#333;padding:12px 18px}

.stars{position:absolute;display:flex;gap:4px;align-items:center}
.t-line{position:absolute;height:1px;background:#ccc}
.quote{position:absolute;width:285px;font-size:13.5px;line-height:24px;color:var(--text)}
.qmark{font-family:"Arvo",serif;font-size:30px;color:#bbb;line-height:10px}
.qopen{display:block;height:20px;font-family:"Arvo",serif;font-size:30px;color:#bbb;line-height:30px}
.author{position:absolute;width:283px;height:58px;background:var(--navy-dark)}
.author .avatar{position:absolute;left:14px;top:6px;width:46px;height:46px;border-radius:50%;background:linear-gradient(135deg,#8a6a55,#c9a58a);border:3px solid var(--white)}
.author .who{position:absolute;left:100px;top:12px;color:var(--white);font-size:13px;line-height:17px}

.footer{top:4292px;left:0;width:1200px;height:444px;background:var(--footer);color:#ccc}
.f-divider{position:absolute;top:0;width:1px;height:300px;background:#444}
.f-head{position:absolute;font-style:italic;font-size:16px;color:var(--white);padding-left:14px;border-left:3px solid var(--orange);line-height:22px}
.f-list{position:absolute;font-size:13px;line-height:25px;color:#ccc;list-style:none}
.f-ico{display:inline-block;width:24px;height:24px;border-radius:50%;background:#555;vertical-align:middle;margin-right:16px}
</style>
</head>
<body>

<div class="abs topbar">
  <svg class="abs topbar-accent" width="1200" height="48"><polygon points="604,0 1200,0 1200,48 576,48" fill="#ff6a0d"/></svg>
  <div class="round-ico" style="left:158px;top:9px"><svg width="14" height="10"><rect x="0.5" y="0.5" width="13" height="9" fill="none" stroke="#fff"/><polyline points="1,1 7,6 13,1" fill="none" stroke="#fff"/></svg></div>
  <div class="contact" style="left:196px;top:6px">Get In Touch<br>info@velasto.com</div>
  <div class="question-pill"></div>
  <div class="round-ico" style="left:822px;top:10px"><svg width="14" height="14" viewBox="0 0 24 24"><path d="M6 2l4 5-2 3c1 3 3 5 6 6l3-2 5 4-3 4C10 22 2 14 2 5z" fill="#fff"/></svg></div>
  <div class="contact" style="left:866px;top:6px">Have any questions?<br>555-014-2280</div>
</div>

<div class="abs nav">
  <div class="logo" style="left:158px;top:6px;font-size:44px;color:var(--ink)">velasto</div>
  <nav class="nav-links"><span class="active">Home</span><span>About</span><span>Solution</span><span>Event</span><span>Contact Us</span></nav>
</div>

<section class="abs hero">
  <div class="abs" role="img" aria-label="Photo of a smiling diverse team of colleagues in an office" style="inset:0;background:radial-gradient(ellipse at 50% 40%,rgba(120,100,85,.5),rgba(30,28,30,.6))"></div>
  <h1 class="heading hero-title">Increase Employee<br>Retention</h1>
  <p class="hero-sub">long established fact that a reader distracted<br>by the readable content</p>
  <div class="btn" style="left:527px;top:310px;width:146px;height:46px">Get In Touch</div>
  <div class="arrow-btn" style="left:159px;top:254px"><svg width="10" height="14"><polyline points="8,1 2,7 8,13" fill="none" stroke="#222" stroke-width="2.4"/></svg></div>
  <div class="arrow-btn" style="left:1009px;top:254px"><svg width="10" height="14"><polyline points="2,1 8,7 2,13" fill="none" stroke="#222" stroke-width="2.4"/></svg></div>
  <svg class="abs" style="left:0;top:424px" width="1200" height="120">
    <path d="M0,120 Q600,-20 1200,120 Z" fill="#fff"/>
    <path d="M0,118 Q600,-22 1200,80" fill="none" stroke="#ff6a0d" stroke-width="5"/>
    <path d="M546,60 A56,40 0 0 0 656,60 Z" fill="#ff6a0d"/>
  </svg>
</section>

<section>
  <div class="dots" style="left:158px;top:688px;width:176px;height:98px"></div>
  <div class="abs" style="left:166px;top:704px;width:398px;height:398px;border-radius:50%;background:var(--orange)"></div>
  <div class="abs" style="left:180px;top:705px;width:370px;height:370px;border-radius:50%;background:var(--white)"></div>
  <div class="abs" role="img" aria-label="Photo of a confident young man leading a group of coworkers" style="left:192px;top:712px;width:352px;height:352px;border-radius:50%;background:linear-gradient(160deg,#e8e6e3,#b9b4ae 55%,#6d6864)"></div>
  <div class="abs" style="left:472px;top:721px;width:56px;height:56px;border-radius:50%;background:var(--orange)"></div>
  <h2 class="section-title abs" style="left:643px;top:752px">About Us</h2>
  <p class="para abs" style="left:643px;top:816px;width:400px">There are many variations of passages of Lorem Ipsum available, but the majority have suffered alteration in some form, by injected humour, or randomised words which don't look even slightly believable.</p>
  <p class="para abs" style="left:643px;top:920px;width:400px">There are many variations of passages of Lorem Ipsum available,</p>
  <div class="btn" style="left:643px;top:982px;width:128px;height:44px">Read More</div>
</section>

<section class="abs schedule">
  <h2 class="heading abs" style="left:158px;top:126px;font-size:40px;line-height:58px;color:var(--white)">Choose A<br>Schedule</h2>
  <p class="abs" style="left:158px;top:246px;width:360px;font-size:14px;line-height:24px;color:#e6e9f0">There are many variations of passages of Lorem Ipsum available, but the majority</p>
  <div class="btn" style="left:158px;top:310px;width:128px;height:44px">View Details</div>
</section>
<div class="abs" style="left:575px;top:1250px;width:28px;height:327px;background:var(--orange)"></div>
<div class="abs" style="left:575px;top:1250px;width:140px;height:24px;background:var(--orange)"></div>
<div class="calendar">
  <table>
    <caption>MARCH 2022</caption>
    <tr><th>Sun</th><th>Mon</th><th>Tue</th><th>Wed</th><th>Thu</th><th>Fri</th><th>Sat</th></tr>
    <tr><td class="mute">27</td><td class="mute">28</td><td>1</td><td>2</td><td>3</td><td>4</td><td>5</td></tr>
    <tr><td>6</td><td>7</td><td>8</td><td>9</td><td>10</td><td>11</td><td>12</td></tr>
    <tr><td>13</td><td>14</td><td>15</td><td>16</td><td>17</td><td>18</td><td>19</td></tr>
    <tr><td>20</td><td>21</td><td>22</td><td>23</td><td>24</td><td>25</td><td>26</td></tr>
    <tr><td>27</td><td>28</td><td>29</td><td>30</td><td>31</td><td class="mute">1</td><td class="mute">2</td></tr>
  </table>
</div>
<div class="abs" style="left:994px;top:1213px;width:48px;height:48px;border-radius:50%;background:var(--orange);color:#fff;font-size:26px;font-weight:700;display:flex;align-items:center;justify-content:center">+</div>

<section class="abs why">
  <svg class="abs" style="left:0;top:0" width="1200" height="560">
    <path d="M0,0 L300,0 C360,60 320,160 240,200 C170,240 120,330 40,360 C20,370 10,400 0,410 Z" fill="#fdf1e8"/>
    <path d="M1200,40 C1130,40 1070,90 1090,160 C1110,230 1200,250 1200,250 Z" fill="#fdf1e8"/>
  </svg>
  <h2 class="section-title abs" style="left:0;top:68px;width:1200px;text-align:center">Why Choose Us</h2>
  <div class="dots" style="left:454px;top:170px;width:118px;height:112px;background-size:10px 10px"></div>
  <div class="dots" style="left:632px;top:330px;width:118px;height:112px;background-size:10px 10px"></div>
  <div class="abs" style="left:454px;top:174px;width:294px;height:294px;border-radius:50%;border:3px solid var(--orange);background:var(--white)"></div>
  <div class="abs" role="img" aria-label="Cheerful cartoon mascot face in orange" style="left:467px;top:187px;width:268px;height:268px;border-radius:50%;background:var(--orange)"></div>

  <div class="feature" style="left:160px;top:176px">
    <div class="pill"></div><div class="frame" style="left:10px"></div>
    <div class="txt" style="left:18px"><b>TRUSTED</b><span>There are many<br>variations</span></div>
    <div class="ico" style="left:182px"><svg width="40" height="40"><circle cx="20" cy="18" r="10" fill="#ff6a0d"/><path d="M6,30 Q20,40 34,30" fill="none" stroke="#ff6a0d" stroke-width="4"/></svg></div>
  </div>
  <div class="feature" style="left:160px;top:349px">
    <div class="pill"></div><div class="frame" style="left:10px"></div>
    <div class="txt" style="left:18px"><b>SUPPORT</b><span>There are many<br>variations</span></div>
    <div class="ico" style="left:182px"><svg width="44" height="30"><rect x="2" y="8" width="40" height="14" rx="7" fill="#ff6a0d"/></svg></div>
  </div>
  <div class="feature" style="left:757px;top:176px">
    <div class="pill"></div><div class="frame" style="left:14px"></div>
    <div class="txt" style="left:18px"><b>VALUED</b><span>There are many<br>variations</span></div>
    <div class="ico" style="left:182px"><svg width="40" height="36"><polygon points="8,4 32,4 38,14 20,34 2,14" fill="#ff6a0d"/></svg></div>
  </div>
  <div class="feature" style="left:757px;top:349px">
    <div class="pill"></div><div class="frame" style="left:14px"></div>
    <div class="txt" style="left:18px"><b>MOTIVATE</b><span>There are many<br>variations</span></div>
    <div class="ico" style="left:182px"><svg width="36" height="40"><circle cx="18" cy="16" r="14" fill="#ff6a0d"/><rect x="10" y="26" width="14" height="12" fill="#ff6a0d"/><polyline points="12,18 18,11 24,18" fill="none" stroke="#fff" stroke-width="3"/></svg></div>
  </div>
</section>

<section class="abs how">
  <div class="abs" role="img" aria-label="Dimmed photo of a team meeting around a table" style="inset:0;background:radial-gradient(ellipse at 70% 50%,rgba(90,90,90,.35),rgba(20,20,20,.2))"></div>
  <div class="abs" style="left:458px;top:46px;width:162px;height:60px;background:var(--orange)"></div>
  <div class="abs" style="left:158px;top:85px;width:427px;height:283px;background:var(--orange)"></div>
  <div class="abs" role="img" aria-label="Video still of colleagues working together at a laptop" style="left:180px;top:64px;width:425px;height:282px;border:3px solid #ddd;background:linear-gradient(135deg,#c9c2b6,#8e8475 50%,#5d5a55)"></div>
  <div class="abs" style="left:352px;top:163px;width:84px;height:84px;border-radius:50%;background:rgba(255,255,255,.55);display:flex;align-items:center;justify-content:center">
    <svg width="34" height="38"><polygon points="4,2 32,19 4,36" fill="#e8141b"/></svg>
  </div>
  <h2 class="heading abs" style="left:651px;top:102px;font-size:40px;color:var(--white)">How It Works</h2>
  <p class="abs" style="left:651px;top:164px;width:400px;font-size:14px;line-height:24px;color:#e2e2e2">There are many variations of passages of Lorem Ipsum available, but the majority have suffered alteration in some form, by injected humour, or randomised words which don't look even slightly believable.</p>
  <div class="btn" style="left:651px;top:280px;width:134px;height:44px">Watch Video</div>
</section>

<section>
  <div class="dots" style="left:0;top:2630px;width:116px;height:66px"></div>
  <div class="dots" style="left:1090px;top:3232px;width:110px;height:66px"></div>
  <h2 class="section-title abs" style="left:0;top:2680px;width:1200px;text-align:center">Events</h2>
  <div class="photo" role="img" aria-label="Photo of two women smiling during a meeting at laptops" style="left:160px;top:2752px;width:425px;height:281px;background:linear-gradient(135deg,#eae8e4,#c8c3bd 55%,#8b8680)"></div>
  <div class="event-date" style="left:158px;top:3056px"><svg width="14" height="14"><rect x="1" y="2" width="12" height="11" fill="none" stroke="#222" stroke-width="1.6"/><line x1="1" y1="5" x2="13" y2="5" stroke="#222" stroke-width="1.6"/></svg>11.03.22</div>
  <div class="event-title" style="left:158px;top:3084px;width:300px">Lorem Ipsum is simply dummy text</div>
  <p class="para abs" style="left:158px;top:3146px;width:360px">There are many variations of passages of Lorem Ipsum available, but the majority</p>

  <div class="photo" role="img" aria-label="Photo of three colleagues looking at a tablet" style="left:610px;top:2752px;width:166px;height:121px;background:linear-gradient(135deg,#d8d6d2,#6d6a68)"></div>
  <div class="photo" role="img" aria-label="Photo of a team seated in a training room" style="left:610px;top:2889px;width:166px;height:122px;background:linear-gradient(135deg,#b8b2a8,#4c4945)"></div>
  <div class="photo" role="img" aria-label="Photo of a smiling woman working at a desk" style="left:610px;top:3029px;width:166px;height:122px;background:linear-gradient(135deg,#f0eeeb,#a9a39d)"></div>

  <div class="event-date" style="left:790px;top:2774px"><svg width="14" height="14"><rect x="1" y="2" width="12" height="11" fill="none" stroke="#222" stroke-width="1.6"/><line x1="1" y1="5" x2="13" y2="5" stroke="#222" stroke-width="1.6"/></svg>11.03.22</div>
  <div class="event-title" style="left:790px;top:2800px;width:260px">Lorem Ipsum is simply dummy text</div>
  <div class="event-date" style="left:790px;top:2911px"><svg width="14" height="14"><rect x="1" y="2" width="12" height="11" fill="none" stroke="#222" stroke-width="1.6"/><line x1="1" y1="5" x2="13" y2="5" stroke="#222" stroke-width="1.6"/></svg>11.03.22</div>
  <div class="event-title" style="left:790px;top:2937px;width:260px">Lorem Ipsum is simply dummy text</div>
  <div class="event-date" style="left:790px;top:3049px"><svg width="14" height="14"><rect x="1" y="2" width="12" height="11" fill="none" stroke="#222" stroke-width="1.6"/><line x1="1" y1="5" x2="13" y2="5" stroke="#222" stroke-width="1.6"/></svg>11.03.22</div>
  <div class="event-title" style="left:790px;top:3075px;width:260px">Lorem Ipsum is simply dummy text</div>

  <div class="btn" style="left:537px;top:3200px;width:126px;height:44px">View All</div>
</section>

<section class="abs contact-sec">
  <div class="abs" role="img" aria-label="Orange-tinted photo of colleagues in a workshop" style="inset:0;background:radial-gradient(ellipse at 50% 60%,rgba(120,50,10,.25),rgba(255,120,40,.1))"></div>
  <svg class="abs" style="left:0;top:0" width="1200" height="80">
    <path d="M0,0 L1200,0 L1200,22 Q600,-40 0,22 Z" fill="#fff"/>
    <path d="M0,22 Q600,-36 1200,22 L1200,30 Q600,-28 0,30 Z" fill="#111"/>
    <path d="M556,28 A46,40 0 0 1 650,28 Z" fill="#fff"/>
    <path d="M562,28 A40,34 0 0 1 644,28 Z" fill="#ff6a0d"/>
  </svg>
  <h2 class="heading abs" style="left:0;top:104px;width:1200px;text-align:center;font-size:40px;color:var(--white)">Contact Us</h2>
  <div class="field" style="left:370px;top:171px;width:228px;height:39px">First Name</div>
  <div class="field" style="left:601px;top:171px;width:229px;height:39px">Last Name</div>
  <div class="field" style="left:370px;top:222px;width:228px;height:39px">Email Address</div>
  <div class="field" style="left:601px;top:222px;width:229px;height:39px">Phone No</div>
  <div class="field" style="left:370px;top:276px;width:460px;height:112px;border-radius:0">Message</div>
  <div class="btn" style="left:537px;top:401px;width:126px;height:44px;background:#111;font-size:14px">Submit Now</div>
</section>

<section>
  <h2 class="section-title abs" style="left:0;top:3848px;width:1200px;text-align:center">Testimonial</h2>

  <div class="stars" style="left:158px;top:3922px"><svg width="104" height="18"><g fill="#ffb400"><polygon points="9,1 11.5,6.5 17,7 13,11 14,17 9,14 4,17 5,11 1,7 6.5,6.5"/><polygon transform="translate(21,0)" points="9,1 11.5,6.5 17,7 13,11 14,17 9,14 4,17 5,11 1,7 6.5,6.5"/><polygon transform="translate(42,0)" points="9,1 11.5,6.5 17,7 13,11 14,17 9,14 4,17 5,11 1,7 6.5,6.5"/><polygon transform="translate(63,0)" points="9,1 11.5,6.5 17,7 13,11 14,17 9,14 4,17 5,11 1,7 6.5,6.5"/><polygon transform="translate(84,0)" points="9,1 11.5,6.5 17,7 13,11 14,17 9,14 4,17 5,11 1,7 6.5,6.5"/></g></svg></div>
  <div class="t-line" style="left:272px;top:3931px;width:170px"></div>
  <div class="quote" style="left:158px;top:3960px"><span class="qopen">&ldquo;</span>There are many variations of passages of Lorem Ipsum available, but the majority have suffered alteration in some form, by injected humour, or randomised words which don't look even slightly believable. <span class="qmark">&rdquo;</span></div>
  <div class="author" style="left:158px;top:4152px"><div class="avatar" role="img" aria-label="Portrait photo of John Doe"></div><div class="who"><b style="font-weight:600">John Doe</b><br>Businessman , USA</div></div>

  <div class="stars" style="left:460px;top:3922px"><svg width="104" height="18"><g fill="#ffb400"><polygon points="9,1 11.5,6.5 17,7 13,11 14,17 9,14 4,17 5,11 1,7 6.5,6.5"/><polygon transform="translate(21,0)" points="9,1 11.5,6.5 17,7 13,11 14,17 9,14 4,17 5,11 1,7 6.5,6.5"/><polygon transform="translate(42,0)" points="9,1 11.5,6.5 17,7 13,11 14,17 9,14 4,17 5,11 1,7 6.5,6.5"/><polygon transform="translate(63,0)" points="9,1 11.5,6.5 17,7 13,11 14,17 9,14 4,17 5,11 1,7 6.5,6.5"/><polygon transform="translate(84,0)" points="9,1 11.5,6.5 17,7 13,11 14,17 9,14 4,17 5,11 1,7 6.5,6.5"/></g></svg></div>
  <div class="t-line" style="left:574px;top:3931px;width:170px"></div>
  <div class="quote" style="left:460px;top:3960px"><span class="qopen">&ldquo;</span>There are many variations of passages of Lorem Ipsum available, but the majority have suffered alteration in some form, by injected humour, or randomised words which don't look even slightly believable. <span class="qmark">&rdquo;</span></div>
  <div class="author" style="left:460px;top:4152px"><div class="avatar" role="img" aria-label="Portrait photo of John Smith"></div><div class="who"><b style="font-weight:600">John Smith</b><br>Businessman , USA</div></div>

  <div class="stars" style="left:759px;top:3922px"><svg width="104" height="18"><g fill="#ffb400"><polygon points="9,1 11.5,6.5 17,7 13,11 14,17 9,14 4,17 5,11 1,7 6.5,6.5"/><polygon transform="translate(21,0)" points="9,1 11.5,6.5 17,7 13,11 14,17 9,14 4,17 5,11 1,7 6.5,6.5"/><polygon transform="translate(42,0)" points="9,1 11.5,6.5 17,7 13,11 14,17 9,14 4,17 5,11 1,7 6.5,6.5"/><polygon transform="translate(63,0)" points="9,1 11.5,6.5 17,7 13,11 14,17 9,14 4,17 5,11 1,7 6.5,6.5"/><polygon transform="translate(84,0)" points="9,1 11.5,6.5 17,7 13,11 14,17 9,14 4,17 5,11 1,7 6.5,6.5"/></g></svg></div>
  <div class="t-line" style="left:873px;top:3931px;width:169px"></div>
  <div class="quote" style="left:759px;top:3960px"><span class="qopen">&ldquo;</span>There are many variations of passages of Lorem Ipsum available, but the majority have suffered alteration in some form, by injected humour, or randomised words which don't look even slightly believable. <span class="qmark">&rdquo;</span></div>
  <div class="author" style="left:759px;top:4152px"><div class="avatar" role="img" aria-label="Portrait photo of John Doe"></div><div class="who"><b style="font-weight:600">John Doe</b><br>Businessman , USA</div></div>

  <svg class="abs" style="left:570px;top:4230px" width="60" height="14"><circle cx="10" cy="7" r="4.5" fill="#ff6a0d"/><circle cx="30" cy="7" r="4" fill="none" stroke="#777"/><circle cx="50" cy="7" r="4" fill="none" stroke="#777"/></svg>
</section>

<footer class="abs footer">
  <div class="f-divider" style="left:400px"></div>
  <div class="f-divider" style="left:680px"></div>
  <div class="f-divider" style="left:884px"></div>
  <div class="logo" style="left:158px;top:94px;font-size:36px;color:var(--white)">velasto</div>
  <p class="abs" style="left:158px;top:146px;width:225px;font-size:13px;line-height:23px;color:#ccc">There are many variations of passages of Lorem Ipsum available, but the majority have suffered alteration in some form, by injected humour, or randomised .</p>

  <div class="f-head" style="left:400px;top:99px">Contact US</div>
  <svg class="abs" style="left:425px;top:150px" width="28" height="28"><circle cx="14" cy="14" r="14" fill="#fff"/><path d="M14,6 a5,5 0 0 1 5,5 c0,4 -5,10 -5,10 c0,0 -5,-6 -5,-10 a5,5 0 0 1 5,-5z" fill="#ff6a0d"/></svg>
  <p class="abs" style="left:469px;top:144px;width:200px;font-size:13px;line-height:19px;color:#ccc">Two Harbor Point<br>4410 Lakeside Drive<br>Denver CO, 80202</p>
  <svg class="abs" style="left:425px;top:209px" width="28" height="28"><circle cx="14" cy="14" r="14" fill="#fff"/><rect x="7" y="9" width="14" height="10" fill="#ff6a0d"/><polyline points="7,9 14,15 21,9" fill="none" stroke="#fff" stroke-width="1.2"/></svg>
  <p class="abs" style="left:469px;top:213px;font-size:13px;color:#ccc">info@velasto.com</p>
  <svg class="abs" style="left:425px;top:254px" width="28" height="28"><circle cx="14" cy="14" r="14" fill="#fff"/><path d="M9 7l3 4-1.5 2c.8 2 2.3 3.5 4.5 4.5l2-1.5 4 3-2 3C12 22 6 16 6 9z" fill="#ff6a0d"/></svg>
  <p class="abs" style="left:469px;top:258px;font-size:13px;color:#ccc">555-014-2280</p>

  <div class="f-head" style="left:680px;top:99px">Company</div>
  <ul class="f-list" style="left:726px;top:144px">
    <li>&rarr;&nbsp;&nbsp;&nbsp;&nbsp;Home</li><li>&rarr;&nbsp;&nbsp;&nbsp;&nbsp;About</li><li>&rarr;&nbsp;&nbsp;&nbsp;&nbsp;Solution</li><li>&rarr;&nbsp;&nbsp;&nbsp;&nbsp;Event</li><li>&rarr;&nbsp;&nbsp;&nbsp;&nbsp;Contact Us</li>
  </ul>

  <div class="f-head" style="left:884px;top:99px">Follow Us</div>
  <ul class="f-list" style="left:934px;top:144px;line-height:31px">
    <li><span class="f-ico"></span>Friendly</li><li><span class="f-ico"></span>Chirpo</li><li><span class="f-ico"></span>Linkora</li><li><span class="f-ico"></span>Snapgrid</li><li><span class="f-ico"></span>Vidstream</li>
  </ul>

  <p class="abs" style="left:0;top:370px;width:1200px;text-align:center;font-size:12px;color:#ccc">Copyright&copy;2022 <b style="color:#fff">velasto</b> , All Rights Reserved.</p>
</footer>

</body>
</html>
```